San Francisco Leading Consulting firm - 47Nova Web Design Project

•Create a Web Design
•Uncoded webpage layout design
•2 Pages Design - Homepage + Interior Page

Task Description
Hello, we're looking for a re-design our current website www.47nova-example.com

we have a sample mockup design @

http://47nova.civicpane-example.org/

This shows the layout that we like and also a sample of 6 pictures that would change based on where you mouse over..

6 pictures HOME design needs to be included.

SMART
THOUGHTFUL
FLEXIBLE
CREATIVE SERVICES
TECHNICAL SERVICES
PARTNERS

sites we like:

http://www.brelmoradvisory-example.com/Home.cfm?id=Home
http://www.pixelquarry-example.com/index.html

Our company can be best described as: 100+ employees, cutting-edge, depandable, innovative, strong, smart.

Our Primary focus is: IT Consulting Services and Creative Design services

47Nova LLC is a consulting firm providing creative design, business and technology solutions to both private and public interests.

Established in 1996, 47Nova is a San Francisco based company providing specialists for a range of business needs including:

Creative Design Services
•Print
•Logo Design
•Website Design
•Illustration

and

Business and Technology solutions

•Application Software and Web Development
•Business Process Re-Design (BPR)
•Business/Systems Analysis and Requirement Documentation
•Mentoring and Training
•Network/Hardware Installation Services
•System Design and Architecture
•Vendor Management
•Teamvault Architecture and Implementation

our sample mockup site:

Reason: Due to holiday season, we're not available to work with designers and finilize our design.  

Thank you very much for submitting your design.

We appreciate your time and creativity.   Since, our office is currently closed for holidays, we will be reviewing it in details next week and will make our decision as soon as possible.

It would be great if you could submit any of your changes by Wed next week, so it would be part of our reviews. 

Please see updated wireframe under attachments:  we have some minor updates to our wireframe that we would like you to update your designs, if possible.  

We also encorouge you not to use our standard wireframe and come up with more unique designs.   Everything would be considered when we review your design.

 

Target Market(s)

Creative services and professional services clients, including government agencies

Industry/Entity Type

Business

Requirements
Must have
• Clean, professional look, easy navigation

```html
<!DOCTYPE html>
<html lang="en">
<head>
<meta charset="utf-8">
<title>47Nova — Technology Solutions for the 21st Century</title>
<link href="https://fonts.googleapis.com/css2?family=Open+Sans:ital,wght@0,400;0,600;0,700;1,400&display=swap" rel="stylesheet">
<style>
  :root {
    --header-bg: #eef6fa;
    --nav-bg: #dcebf3;
    --ink: #333a40;
    --ink-soft: #6b7378;
    --accent-blue: #1f7fc0;
    --link-blue: #1a6fb6;
    --welcome-cyan: #3fd0ef;
    --chevron: #f0a21b;
    --slide-blue-1: #6cb6e6;
    --slide-blue-2: #2f76c4;
    --card-line: #dfe3e6;
    --creative-blue: #2a8fd0;
    --tech-red: #9a3b4b;
    --partner-green: #8db43a;
    --partner-green-dark: #6f9428;
    --quote-blue: #a8d5ec;
  }
  * { box-sizing: border-box; margin: 0; padding: 0; }
  html, body { width: 1159px; height: 1200px; overflow: hidden; }
  body {
    position: relative;
    font-family: "Open Sans", Arial, sans-serif;
    color: var(--ink);
    background: linear-gradient(#e6e8ea 300px, #eceef0 611px, #f3f4f5 760px, #fafbfb 1000px, #ffffff 1200px);
  }
  .abs { position: absolute; }

  /* Header */
  .site-header { left: 0; top: 0; width: 1159px; height: 100px; background: var(--header-bg); }
  .brand { left: 147px; top: 38px; display: flex; align-items: center; gap: 8px; }
  .brand-mark { width: 22px; height: 22px; border-radius: 50%; background: var(--accent-blue); }
  .brand-name { font-size: 27px; font-weight: 400; color: #2b3035; letter-spacing: 0.5px; }
  .tagline { left: 333px; top: 50px; font-size: 12.5px; color: var(--ink); }
  .contact { left: 923px; top: 14px; font-size: 11.5px; color: var(--ink-soft); line-height: 1.25; }
  .contact .phone { font-size: 16.5px; color: var(--accent-blue); margin-bottom: 6px; }
  .contact .email { color: var(--accent-blue); font-size: 12px; }

  /* Navigation */
  .main-nav { left: 0; top: 100px; width: 1159px; height: 36px; background: var(--nav-bg); }
  .nav-item { top: 11px; font-size: 10.5px; font-weight: 700; letter-spacing: 0.6px; color: #2f3438; }
  .nav-item .chev { color: var(--chevron); margin-left: 10px; font-weight: 700; }
  .search { left: 872px; top: 8px; width: 150px; height: 21px; background: #fff; border: 1px solid #cfdde6; border-radius: 2px; font-size: 7.5px; font-style: italic; color: #9aa3a8; padding: 5px 7px; }
  .search svg { position: absolute; right: 5px; top: 4px; }

  /* Welcome */
  .welcome { left: 0; top: 136px; width: 1159px; height: 164px; background: #fff; }
  .welcome h1 { position: absolute; left: 152px; top: 30px; font-size: 37px; font-weight: 400; color: var(--welcome-cyan); }
  .welcome p { position: absolute; left: 152px; font-size: 11.2px; letter-spacing: -0.1px; color: var(--ink); white-space: nowrap; }

  /* Slider */
  .slider { left: 137px; top: 300px; width: 881px; height: 311px; }
  .slide-lead { left: 0; top: 0; width: 284px; height: 311px; background: linear-gradient(160deg, var(--slide-blue-1), var(--slide-blue-2)); }
  .slide-word { left: 58px; top: 128px; font-size: 43px; color: #fff; font-weight: 400; }
  .slide-photo-a { left: 284px; top: 0; width: 312px; height: 311px; background: linear-gradient(135deg, #c9c2b4, #8a8276 55%, #ece9e2); }
  .slide-photo-b { left: 597px; top: 0; width: 236px; height: 311px; background: linear-gradient(160deg, #f2eeea, #a9a6a3 50%, #3d3f42); border-left: 2px solid #5aa8e2; }
  .slide-tail { left: 833px; top: 0; width: 48px; height: 311px; background: linear-gradient(#5aa6e0, #2f76c4); }
  .dots { left: 17px; top: 292px; display: flex; gap: 5px; }
  .dots span { width: 6px; height: 6px; border-radius: 50%; background: #9fc6ea; }
  .dots span.active { background: #fff; }

  /* Service cards */
  .card { top: 648px; width: 256px; height: 147px; background: linear-gradient(#fff, #f5f6f7); border: 1px solid var(--card-line); border-radius: 8px; box-shadow: 0 2px 4px rgba(0,0,0,0.05); }
  .card-icon { position: absolute; left: 22px; top: 38px; }
  .card-title { position: absolute; font-size: 18px; color: #2f3438; line-height: 1.15; }
  .card-title small { display: block; font-size: 17px; color: #7b8287; }
  .card-more { position: absolute; right: 18px; bottom: 14px; font-size: 11.5px; color: #444; }
  .card-more b { color: var(--chevron); margin-left: 4px; }

  /* Clients & testimonials */
  .clients { left: 144px; top: 865px; width: 584px; height: 86px; background: #fff; border: 1px solid #d6dade; border-radius: 8px; }
  .clients span { position: absolute; left: 15px; top: 31px; font-size: 15px; color: #6a7176; }
  .clients svg { position: absolute; right: 10px; top: 34px; }
  .testimonials { left: 760px; top: 862px; width: 236px; }
  .testimonials h2 { font-size: 15.5px; font-weight: 400; color: #6a7176; }
  .testimonials blockquote { font-size: 10.5px; font-style: italic; color: #7b8287; margin-top: 20px; line-height: 1.3; }
  .testimonials cite { display: block; text-align: right; font-size: 9.5px; font-style: normal; color: #6a7176; margin-top: 6px; }
  .quote-open { left: 760px; top: 880px; font-size: 34px; color: var(--quote-blue); font-family: Georgia, serif; line-height: 1; }
  .quote-close { left: 970px; top: 946px; font-size: 34px; color: var(--quote-blue); font-family: Georgia, serif; line-height: 1; }

  /* Service lists */
  .list-heading { top: 988px; font-size: 13px; font-weight: 700; color: #3b4045; }
  .service-list { list-style: none; }
  .service-list li { position: absolute; font-size: 9.5px; color: var(--link-blue); width: 220px; line-height: 1.35; }
  .service-list li::before { content: "• "; }
  .divider { left: 411px; top: 977px; width: 1px; height: 160px; background: #dde1e4; }

  /* Footer */
  .site-footer { left: 96px; top: 1152px; width: 917px; height: 48px; border-top: 1px solid #e2e5e8; box-shadow: 0 -3px 6px rgba(0,0,0,0.03); }
  .site-footer p { text-align: center; margin-top: 21px; font-size: 10.5px; color: #222; }
</style>
</head>
<body>

<header class="site-header abs">
  <div class="brand abs">
    <span class="brand-mark"></span>
    <span class="brand-name">47Nova</span>
  </div>
  <div class="tagline abs">Thechnology Solutions for the 21st Century</div>
  <div class="contact abs">
    <div>Call us at</div>
    <div class="phone">555.010.0600</div>
    <div>Email us at</div>
    <div class="email">info@47nova-example.com</div>
  </div>
</header>

<nav class="main-nav abs">
  <div class="nav-item abs" style="left:151px">COMPANY<span class="chev">›</span></div>
  <div class="nav-item abs" style="left:249px">CREATIVE SERVICES<span class="chev">›</span></div>
  <div class="nav-item abs" style="left:408px">TECHNICAL SERVICES<span class="chev">›</span></div>
  <div class="nav-item abs" style="left:584px">PARTNERS<span class="chev">›</span></div>
  <div class="nav-item abs" style="left:695px">CONTACT US</div>
  <div class="search abs">SEARCH
    <svg width="12" height="12" viewBox="0 0 12 12"><circle cx="7" cy="5" r="3.5" fill="none" stroke="#f0a21b" stroke-width="1.5"/><line x1="4.5" y1="7.5" x2="1.5" y2="10.5" stroke="#f0a21b" stroke-width="1.8"/></svg>
  </div>
</nav>

<section class="welcome abs">
  <h1>welcome</h1>
  <p style="top:91px">47Nova LLC is a consulting firm providing creative design, business and technology solutions to both private and public interests.</p>
  <p style="top:122px">Our experts possess broad industry knowledge which can help with technical and businessprocess challenges, delivering solutions that are creative and cost effective.</p>
</section>

<section class="slider abs">
  <div class="slide-lead abs">
    <svg class="abs" style="left:16px;top:140px" width="16" height="34" viewBox="0 0 16 34"><polyline points="14,2 3,17 14,32" fill="none" stroke="#fff" stroke-width="2.5"/></svg>
    <div class="slide-word abs">thoughtful</div>
    <div class="dots abs"><span></span><span class="active"></span><span></span><span></span><span></span><span></span></div>
  </div>
  <div class="slide-photo-a abs" role="img" aria-label="Photo of two businessmen reviewing documents together"></div>
  <div class="slide-photo-b abs" role="img" aria-label="Close-up photo of hands typing on a keyboard"></div>
  <div class="slide-tail abs">
    <svg class="abs" style="left:17px;top:140px" width="16" height="34" viewBox="0 0 16 34"><polyline points="2,2 13,17 2,32" fill="none" stroke="#fff" stroke-width="2.5"/></svg>
  </div>
</section>

<article class="card abs" style="left:145px">
  <svg class="card-icon" width="44" height="50" viewBox="0 0 44 50">
    <polygon points="4,46 40,46 40,10" fill="none" stroke="var(--creative-blue)" stroke-width="4"/>
    <polygon points="30,33 36,39 36,33" fill="var(--creative-blue)"/>
    <polygon points="26,2 32,7 10,36 4,39 5,32" fill="var(--creative-blue)"/>
  </svg>
  <div class="card-title" style="left:78px;top:45px">Creative<small>Services</small></div>
  <div class="card-more">Lean More<b>›</b></div>
</article>

<article class="card abs" style="left:449px">
  <svg class="card-icon" width="44" height="50" viewBox="0 0 44 50">
    <path d="M6,42 L26,18 A9,9 0 1 1 34,26 L12,46 Z" fill="var(--tech-red)"/>
    <circle cx="33" cy="13" r="4" fill="#fff"/>
    <polygon points="22,48 22,36 17,36 25,27 33,36 28,36 28,48" fill="var(--tech-red)" stroke="#fff" stroke-width="1.5"/>
  </svg>
  <div class="card-title" style="left:74px;top:42px">Business &amp; Technical<small>Services</small></div>
  <div class="card-more">Lean More<b>›</b></div>
</article>

<article class="card abs" style="left:753px">
  <svg class="card-icon" width="56" height="44" viewBox="0 0 56 44" style="left:22px;top:44px">
    <polygon points="1,14 11,5 20,17 10,26" fill="var(--partner-green)"/>
    <polygon points="55,14 45,5 36,17 46,26" fill="var(--partner-green)"/>
    <path d="M13,21 L25,11 L33,12 L43,21 L33,34 L24,34 Z" fill="var(--partner-green)"/>
    <path d="M25,14 L31,20 M22,19 L29,26 M20,24 L26,30" stroke="#fff" stroke-width="1.6" fill="none"/>
    <path d="M33,12 L24,20" stroke="var(--partner-green-dark)" stroke-width="1.6" fill="none"/>
  </svg>
  <div class="card-title" style="left:89px;top:62px">Partners</div>
  <div class="card-more">Lean More<b>›</b></div>
</article>

<section class="clients abs">
  <span>Our Clinets</span>
  <svg width="10" height="16" viewBox="0 0 10 16"><polyline points="2,1 8,8 2,15" fill="none" stroke="#777" stroke-width="2"/></svg>
</section>

<aside class="testimonials abs">
  <h2>Testimonials</h2>
  <blockquote>Lorem ipsum dolor sit amet, consectetuer ading elit, sed diam nonummy nibh euismod.
    <cite>Dana Merrow, CEO of Company</cite>
  </blockquote>
</aside>
<div class="quote-open abs">“</div>
<div class="quote-close abs">”</div>

<h3 class="list-heading abs" style="left:146px">Creative Design Services</h3>
<ul class="service-list">
  <li style="left:160px;top:1022px">Print</li>
  <li style="left:160px;top:1048px">Logo Design</li>
  <li style="left:160px;top:1073px">Website Design</li>
  <li style="left:160px;top:1099px">Illustration</li>
</ul>
<div class="divider abs"></div>
<h3 class="list-heading abs" style="left:459px">Business and Technical solutions</h3>
<ul class="service-list">
  <li style="left:473px;top:1022px;width:240px">Application Software and Web Development</li>
  <li style="left:473px;top:1048px">Business Process Re-Design (BPR)</li>
  <li style="left:473px;top:1073px;width:230px">Business/Systems Analysis and Requirement<br>&nbsp;&nbsp;Documentation</li>
  <li style="left:473px;top:1111px">Mentoring and Training</li>
  <li style="left:731px;top:1022px;width:260px">Network/Hardware Installation Services</li>
  <li style="left:731px;top:1048px">System Design and Architecture</li>
  <li style="left:731px;top:1073px">Vendor Management</li>
  <li style="left:731px;top:1099px;width:260px">Teamvault Architecture and Implementation</li>
</ul>

<footer class="site-footer abs">
  <p>Copyright 2010, 47Nova, LLC All rights reserved.</p>
</footer>

</body>
</html>
```